Business Card Design

We are a flooring/granite/cabinet company
want a sleek and modern design card. Will send our logo. maybe our logo in 3d on card.
black card

Industry/Entity Type

Business

Contact Information for Business Card

Gregory Tallis
company name Stone Hearth Depot
4827 fm 71s 78540
210-634-8872
stonehearthdepot@mailvista.example

```html
<!DOCTYPE html>
<html lang="en">
<head>
<meta charset="utf-8">
<title>Stone Hearth Depot – Business Card</title>
<link rel="stylesheet" href="https://fonts.googleapis.com/css2?family=Barlow:wght@300;400;500;700&display=swap">
<style>
  :root {
    --page: #d8d8d8;
    --card-black: #0c0c0d;
    --card-sheen: #2a2a2c;
    --steel: #9a9a9c;
    --brand-blue: #234b6e;
    --band-grey: #8c8c8e;
    --text-light: #f2f2f2;
    --text-muted: #8a8a8c;
  }
  * { box-sizing: border-box; margin: 0; padding: 0; }
  html, body { width: 1200px; height: 861px; overflow: hidden; }
  body {
    background: var(--page);
    font-family: "Barlow", Arial, sans-serif;
    display: flex;
    align-items: center;
    justify-content: center;
    gap: 40px;
  }
  .card {
    position: relative;
    width: 540px;
    height: 309px;
    background: var(--card-black);
    overflow: hidden;
    box-shadow: 0 6px 18px rgba(0,0,0,.25);
  }

  /* Front */
  .card--front {
    background: radial-gradient(ellipse at 50% 40%, var(--card-sheen) 0%, var(--card-black) 70%);
    display: flex;
    align-items: center;
    justify-content: center;
    gap: 14px;
  }
  .brand-mark {
    width: 22px; height: 22px;
    background: var(--steel);
  }
  .brand-name {
    font-weight: 700;
    font-size: 30px;
    letter-spacing: 1px;
    text-transform: uppercase;
    color: var(--steel);
  }

  /* Back */
  .identity {
    position: absolute;
    left: 40px; top: 34px;
  }
  .identity__brand {
    display: flex; align-items: center; gap: 10px;
  }
  .identity__brand .brand-mark { width: 16px; height: 16px; background: var(--brand-blue); }
  .identity__brand .brand-name { font-size: 21px; color: var(--brand-blue); }
  .person { margin-top: 26px; }
  .person__name {
    font-weight: 700; font-size: 21px; letter-spacing: 1px;
    text-transform: uppercase; color: var(--brand-blue);
  }
  .person__title {
    font-weight: 400; font-size: 10px; letter-spacing: .6px;
    text-transform: uppercase; color: var(--text-muted);
  }
  .contacts {
    position: absolute;
    left: 0; right: 0; top: 160px;
    display: flex; flex-direction: column; gap: 14px;
  }
  .contact {
    position: relative;
    height: 28px;
    background: var(--band-grey);
    display: flex; align-items: center; justify-content: center;
    color: var(--text-light);
    font-size: 12.5px; font-weight: 500; letter-spacing: .4px;
  }
  .contact__icon {
    position: absolute; top: 0;
    width: 28px; height: 28px;
    background: var(--brand-blue);
    display: flex; align-items: center; justify-content: center;
  }
  .contact__icon--left { left: 18px; }
  .contact__icon--right { right: 18px; }
  .contact__icon svg { width: 14px; height: 14px; fill: var(--text-light); }
</style>
</head>
<body>
  <svg width="0" height="0" style="position:absolute">
    <defs>
      <symbol id="icon-phone" viewBox="0 0 24 24"><path d="M6.6 10.8a15 15 0 0 0 6.6 6.6l2.2-2.2c.3-.3.7-.4 1-.2 1.1.4 2.3.6 3.6.6.6 0 1 .4 1 1V20c0 .6-.4 1-1 1A17 17 0 0 1 3 4c0-.6.4-1 1-1h3.5c.6 0 1 .4 1 1 0 1.3.2 2.5.6 3.6.1.3 0 .7-.2 1z"/></symbol>
      <symbol id="icon-mail" viewBox="0 0 24 24"><path d="M2 5h20v14H2z M3 6.5v1l9 6 9-6v-1l-9 6z" fill-rule="evenodd"/></symbol>
      <symbol id="icon-pin" viewBox="0 0 24 24"><path d="M12 2a7 7 0 0 0-7 7c0 5 7 13 7 13s7-8 7-13a7 7 0 0 0-7-7zm0 9.5A2.5 2.5 0 1 1 12 6.5a2.5 2.5 0 0 1 0 5z"/></symbol>
    </defs>
  </svg>

  <section class="card card--front" aria-label="Card front">
    <span class="brand-mark"></span>
    <span class="brand-name">Stone Hearth Depot</span>
  </section>

  <section class="card card--back" aria-label="Card back">
    <div class="identity">
      <div class="identity__brand">
        <span class="brand-mark"></span>
        <span class="brand-name">Stone Hearth Depot</span>
      </div>
      <div class="person">
        <p class="person__name">Gregory Tallis</p>
        <p class="person__title">President of Operations</p>
      </div>
    </div>

    <div class="contacts">
      <div class="contact contact--phone">
        <span class="contact__icon contact__icon--left"><svg><use href="#icon-phone"/></svg></span>
        210-634-8872
        <span class="contact__icon contact__icon--right"><svg><use href="#icon-phone"/></svg></span>
      </div>
      <div class="contact contact--email">
        <span class="contact__icon contact__icon--left"><svg><use href="#icon-mail"/></svg></span>
        stonehearthdepot@mailvista.example
        <span class="contact__icon contact__icon--right"><svg><use href="#icon-mail"/></svg></span>
      </div>
      <div class="contact contact--address">
        <span class="contact__icon contact__icon--left"><svg><use href="#icon-pin"/></svg></span>
        4827 FM 71 South, Stonebridge, Texas 78540
        <span class="contact__icon contact__icon--right"><svg><use href="#icon-pin"/></svg></span>
      </div>
    </div>
  </section>
</body>
</html>
```